Web App Dashboard Design for Healthcare Company

We have developed a simple web application with 3 navigation menus. We like the current design (very much modeled after Tallyworks), but we want to explore UI options for the branding, header, menus, and footer that we may not have considered.

The attached screenshots show the layout and two menu "hover" views as they currently exist.

This web application is used by employees only.

Menu 1 - Module Menu:
Allows the user to switch easily between Account, Employee, and Care Management.

Menu 2 - Reports Menu
Allows user to view available reports within each Module.

Menu 3 - Admin Menu
Allows the user to easily create new content types within each module.

Use our branded colors and font.

Colors:
Logo Blue (dark): 00c0f3
Logo Blue (light): 44c8f5
Nav Blue: 0994d0
Green: 71b44b
Grayscale: (not specified)

Font:
Lato (Google Font)

Target Market(s)

Internal staff.

Industry/Entity Type

Healthcare

Number of Pages Required

3 page

Font styles to use
Sans Serif
Other font styles liked:
• Lato (Google Font)

Colors
0293ce
9bcb3c

Requirements
Must have
• It's really a one page design, but we want to see the two "hover" views for the Module Menu and the Admin Menu.
• It should also be very clear which "Report" page the user is on (the active menu link).
• Must use branded colors, font, and logo.
• Logo Blue (dark): 00c0f3
• Logo Blue (light): 44c8f5
• Nav Blue: 0994d0
• Green: 71b44b
• Grayscale: Designer may choose
Nice to have
• It would be nice to have simple uncluttered payouts.
Should not have
• The design should not have menu options exposed by default.

```html
<!DOCTYPE html>
<html lang="en">
<head>
<meta charset="utf-8">
<title>CareTrackr – Account Management</title>
<link href="https://fonts.googleapis.com/css2?family=Lato:wght@300;400;700&display=swap" rel="stylesheet">
<style>
:root{
  --nav-blue:#0994d0;
  --logo-blue:#00c0f3;
  --green:#71b44b;
  --green-light:#9bcb3c;
  --red:#f25f5c;
  --yellow:#fbbc05;
  --purple:#b07ae8;
  --page:#f2f2f2;
  --card:#ffffff;
  --line:#e6e6e6;
  --ink:#333333;
  --ink-soft:#555555;
  --muted:#999999;
  --topbar:#333333;
}
*{box-sizing:border-box;margin:0;padding:0}
html,body{width:1200px;height:1022px;overflow:hidden}
body{font-family:"Lato",sans-serif;background:var(--page);color:var(--ink);position:relative}
svg{display:block}

.topbar{height:7px;background:var(--topbar)}
.header{position:absolute;top:7px;left:0;width:1200px;height:81px;background:var(--card)}
.brand{position:absolute;left:26px;top:26px;display:flex;align-items:center;gap:8px;font-weight:700;font-size:22px;color:var(--ink)}
.brand-dot{width:14px;height:14px;border-radius:50%;background:var(--logo-blue)}
.module-select{position:absolute;left:194px;top:24px;width:392px;height:36px;border-radius:18px;background:#efefef;font-size:15px;color:var(--ink);padding:0 22px;display:flex;align-items:center;justify-content:space-between}
.icon-btn{position:absolute;top:28px;width:24px;height:24px}
.badge{position:absolute;top:-6px;right:-6px;width:14px;height:14px;border-radius:50%;background:var(--green);color:#fff;font-size:9px;font-weight:700;display:flex;align-items:center;justify-content:center}
.header-divider{position:absolute;top:0;height:81px;width:1px;background:var(--line)}
.user{position:absolute;left:892px;top:17px;display:flex;align-items:center;gap:12px}
.avatar{border-radius:50%;flex:none}
.user-name{font-size:17px;line-height:18px;color:var(--ink)}
.user-name span{display:block;font-size:13px;color:var(--muted)}

.card{position:absolute;background:var(--card);border:1px solid var(--line)}
.card-head{height:43px;background:var(--nav-blue);color:#fff;display:flex;align-items:center;justify-content:space-between;padding:0 16px;font-size:17px;font-weight:700}
.card-filter{font-size:12px;font-weight:400;display:flex;align-items:center;gap:6px}

.tasks{left:26px;top:107px;width:392px;height:461px}
.legend{display:flex;justify-content:center;gap:14px;font-size:12px;color:var(--ink-soft);margin-top:24px}
.legend i{display:inline-block;width:10px;height:10px;border-radius:50%;margin-right:5px;vertical-align:-1px}
.pie{margin:6px auto 0}
.stats{position:absolute;left:16px;right:16px;top:355px;border-top:1px solid var(--line);display:flex;padding-top:18px}
.stat{flex:1;text-align:center;height:72px;font-size:14px;color:var(--ink-soft)}
.stat+.stat{border-left:1px solid var(--line)}
.stat b{display:block;font-size:29px;font-weight:300;color:var(--ink);margin:8px 0 6px}

.reminders{left:437px;top:107px;width:392px;height:461px}
.timeline{position:relative;margin:24px 0 0 22px;height:330px}
.timeline::before{content:"";position:absolute;left:1px;top:2px;bottom:0;width:1px;background:#d8d8d8}
.reminder{position:relative;padding-left:29px;height:79px;font-size:13px;line-height:18px;color:var(--ink-soft)}
.reminder::before{content:"";position:absolute;left:-2px;top:22px;width:8px;height:8px;border-radius:50%;background:var(--green)}
.reminder-date{color:var(--muted);margin-bottom:8px;font-size:14px}
.reminder.is-active::before{background:var(--nav-blue)}
.reminder.is-active .reminder-date{color:var(--ink)}
.reminder.is-active p{color:var(--green);text-decoration:underline}
.btn{position:absolute;left:17px;top:409px;width:106px;height:35px;background:var(--nav-blue);color:#fff;font-size:14px;display:flex;align-items:center;justify-content:center}

.accounts{left:26px;top:588px;width:802px;height:336px}
.account-row{margin:0 16px;height:56px;border-bottom:1px solid var(--line);display:flex;align-items:center;font-size:14px;color:var(--ink)}
.account-row:last-child{border-bottom:0}
.acc-name{width:178px;margin-left:18px}
.acc-tags{width:258px;font-size:12px;color:var(--muted);display:flex;align-items:center;gap:8px}
.acc-time{width:214px;font-size:12px;color:var(--ink);display:flex;align-items:center;gap:6px}
.acc-actions{display:flex;align-items:center;gap:6px;color:#bbb;font-size:12px}

.sidebar{left:864px;top:107px;width:308px;height:817px}
.tabs{display:flex;height:43px;border-bottom:1px solid var(--line)}
.tab{flex:1;display:flex;align-items:center;justify-content:center;font-size:14px;color:var(--muted);border-top:4px solid #c8c8c8;background:#f7f7f7}
.tab+.tab{border-left:1px solid var(--line)}
.tab.is-active{color:var(--ink);border-top-color:var(--nav-blue);background:var(--card);font-weight:700}
.today{padding:24px 17px 14px;border-bottom:1px solid var(--line);font-weight:300}
.today-day{font-size:28px;color:#777}
.today-date{font-size:21px;color:var(--ink);margin-top:4px}
.today-date sup{font-size:11px}
.section-title{font-size:13px;color:var(--ink);padding:22px 17px 16px}
.event{padding:10px 17px 8px;font-size:16px;color:var(--ink-soft);height:53px}
.event.is-hover{background:#f5f5f5}
.event small{display:flex;align-items:center;gap:5px;font-size:11px;color:var(--muted);margin-top:3px}
.events{border-bottom:1px solid var(--line);padding-bottom:14px}
.note{padding:6px 17px 12px;font-size:16px;color:var(--ink-soft)}
.note small{display:block;font-size:11px;color:var(--muted);margin-top:3px}
.notify{position:absolute;left:0;right:0;bottom:0;height:66px;border-top:1px solid var(--line);display:flex;align-items:center;justify-content:space-between;padding:0 17px;font-size:13px;color:var(--ink)}
.switch{width:36px;height:10px;border-radius:5px;background:#a9d88c;position:relative}
.switch::after{content:"";position:absolute;right:-3px;top:-4px;width:17px;height:17px;border-radius:50%;background:var(--green)}

.footer{position:absolute;left:0;bottom:0;width:1200px;height:70px;background:var(--nav-blue);color:#fff;font-size:14px;display:flex;align-items:center;justify-content:space-between;padding:0 26px}
</style>
</head>
<body>
<div class="topbar"></div>

<header class="header">
  <div class="brand"><span class="brand-dot"></span>CareTrackr</div>
  <div class="module-select">Account Management
    <svg width="10" height="6" viewBox="0 0 10 6"><path d="M1 1l4 4 4-4" fill="none" stroke="#666" stroke-width="1.5"/></svg>
  </div>
  <div class="icon-btn" style="left:679px">
    <svg width="22" height="22" viewBox="0 0 22 22" fill="#9a9a9a"><circle cx="7" cy="7" r="3.5"/><circle cx="15" cy="7" r="3.5"/><path d="M1 19c0-4 3-6 6-6s6 2 6 6z"/><path d="M9 19c0-4 3-6 6-6s6 2 6 6z"/></svg>
    <span class="badge">2</span>
  </div>
  <div class="icon-btn" style="left:738px">
    <svg width="22" height="22" viewBox="0 0 22 22" fill="#9a9a9a"><path d="M11 2c-4 0-6 3-6 7v5l-2 3h16l-2-3V9c0-4-2-7-6-7z"/><circle cx="11" cy="19" r="2"/></svg>
    <span class="badge">3</span>
  </div>
  <div class="header-divider" style="left:864px"></div>
  <div class="user">
    <div class="avatar" role="img" aria-label="User profile photo" style="width:44px;height:44px;background:linear-gradient(135deg,#6b6b6b,#2e2e2e);border:2px solid #ddd"></div>
    <div class="user-name">Owen<span>Hartley</span></div>
  </div>
  <div class="header-divider" style="left:1030px"></div>
  <svg class="icon-btn" style="left:1065px" width="18" height="18" viewBox="0 0 18 18"><path d="M9 2v14M2 9h14" stroke="#9a9a9a" stroke-width="2.5"/></svg>
  <div class="header-divider" style="left:1116px"></div>
  <svg class="icon-btn" style="left:1150px" width="18" height="18" viewBox="0 0 18 18"><path d="M7 2H2v14h5" fill="none" stroke="var(--nav-blue)" stroke-width="2"/><path d="M6 9h10M12 5l4 4-4 4" fill="none" stroke="var(--nav-blue)" stroke-width="2"/></svg>
</header>

<section class="card tasks">
  <div class="card-head">Task Distribution<span class="card-filter">This Week <svg width="8" height="5" viewBox="0 0 8 5"><path d="M1 1l3 3 3-3" fill="none" stroke="#fff" stroke-width="1.3"/></svg></span></div>
  <div class="legend">
    <span><i style="background:var(--purple)"></i>Patient Requests</span>
    <span><i style="background:var(--red)"></i>Reports</span>
    <span><i style="background:var(--yellow)"></i>Accounts</span>
  </div>
  <svg class="pie" width="260" height="260" viewBox="-110 -110 220 220" font-family="Lato,sans-serif" font-size="11" fill="#fff" text-anchor="middle">
    <g transform="translate(6,-6)"><path d="M3.1,-87.9 A88,88 0 0 1 87.3,10.7 L37.7,4.6 A38,38 0 0 0 1.3,-38 Z" fill="var(--red)"/><text x="48" y="-37">27%</text></g>
    <g transform="translate(12,8)"><path d="M85,22.8 A88,88 0 0 1 56.6,67.4 L24.4,29.1 A38,38 0 0 0 36.7,9.8 Z" fill="var(--green-light)"/><text x="53" y="37">8%</text></g>
    <g transform="translate(-6,8)"><path d="M44,76.2 A88,88 0 0 1 -82.7,-30.1 L-35.7,-13 A38,38 0 0 0 19,32.9 Z" fill="var(--purple)"/><text x="-40" y="52">38%</text></g>
    <g transform="translate(-6,-6)"><path d="M-77.7,-41.3 A88,88 0 0 1 -12.2,-87.1 L-5.3,-37.6 A38,38 0 0 0 -33.6,-17.8 Z" fill="var(--yellow)"/><text x="-36" y="-48">15%</text></g>
  </svg>
  <div class="stats">
    <div class="stat"><b>59</b>Reports</div>
    <div class="stat"><b>87</b>Patient Requests</div>
    <div class="stat"><b>79</b>Accounts</div>
  </div>
</section>

<section class="card reminders">
  <div class="card-head">Reminders<span class="card-filter">Today <svg width="8" height="5" viewBox="0 0 8 5"><path d="M1 1l3 3 3-3" fill="none" stroke="#fff" stroke-width="1.3"/></svg></span></div>
  <div class="timeline">
    <div class="reminder"><div class="reminder-date">29.62016</div><p>It is a long established fact that a reader will be distracted by the readable ...</p></div>
    <div class="reminder is-active"><div class="reminder-date">29.62016</div><p>It is a long established fact that a reader will be distracted by the readable ...</p></div>
    <div class="reminder"><div class="reminder-date">29.62016</div><p>It is a long established fact that a reader will be distracted by the readable ...</p></div>
    <div class="reminder"><div class="reminder-date">29.62016</div><p>It is a long established fact that a reader will be distracted by the readable ...</p></div>
  </div>
  <div class="btn">View All</div>
</section>

<section class="card accounts">
  <div class="card-head">Accounts<span class="card-filter">Short by: Recent <svg width="8" height="5" viewBox="0 0 8 5"><path d="M1 1l3 3 3-3" fill="none" stroke="#fff" stroke-width="1.3"/></svg></span></div>
  <div class="account-row">
    <div class="avatar" role="img" aria-label="Account holder photo" style="width:38px;height:38px;background:linear-gradient(135deg,#555,#222)"></div>
    <div class="acc-name">Leon Carver</div>
    <div class="acc-tags"><svg width="14" height="10" viewBox="0 0 14 10"><path d="M0 0h9l5 5-5 5H0z" fill="var(--green)"/></svg>Design, Devlopment</div>
    <div class="acc-time"><svg width="12" height="12" viewBox="0 0 12 12"><circle cx="6" cy="6" r="5" fill="none" stroke="#333" stroke-width="1.5"/><path d="M6 3v3h2" fill="none" stroke="#333" stroke-width="1.2"/></svg>This Week 1h:12m <svg width="8" height="5" viewBox="0 0 8 5"><path d="M1 1l3 3 3-3" fill="none" stroke="#777" stroke-width="1.3"/></svg></div>
    <div class="acc-actions"><svg width="11" height="12" viewBox="0 0 11 12"><path d="M1 3h9M4 1h3M2 3l1 8h5l1-8" fill="none" stroke="#aaa" stroke-width="1.3"/></svg>|<svg width="13" height="12" viewBox="0 0 13 12"><path d="M9 1H1v10h9V7M5 7l7-6" fill="none" stroke="#aaa" stroke-width="1.3"/></svg></div>
  </div>
  <div class="account-row">
    <div class="avatar" role="img" aria-label="Account holder photo" style="width:38px;height:38px;background:linear-gradient(135deg,#e8c9a8,#b88a66)"></div>
    <div class="acc-name">Nadia L. Brooks</div>
    <div class="acc-tags"><svg width="14" height="10" viewBox="0 0 14 10"><path d="M0 0h9l5 5-5 5H0z" fill="var(--green)"/></svg>Copywriting, Photography</div>
    <div class="acc-time"><svg width="12" height="12" viewBox="0 0 12 12"><circle cx="6" cy="6" r="5" fill="none" stroke="#333" stroke-width="1.5"/><path d="M6 3v3h2" fill="none" stroke="#333" stroke-width="1.2"/></svg>This Week 1h:12m <svg width="8" height="5" viewBox="0 0 8 5"><path d="M1 1l3 3 3-3" fill="none" stroke="#777" stroke-width="1.3"/></svg></div>
    <div class="acc-actions"><svg width="11" height="12" viewBox="0 0 11 12"><path d="M1 3h9M4 1h3M2 3l1 8h5l1-8" fill="none" stroke="#aaa" stroke-width="1.3"/></svg>|<svg width="13" height="12" viewBox="0 0 13 12"><path d="M9 1H1v10h9V7M5 7l7-6" fill="none" stroke="#aaa" stroke-width="1.3"/></svg></div>
  </div>
  <div class="account-row">
    <div class="avatar" role="img" aria-label="Account holder photo" style="width:38px;height:38px;background:linear-gradient(135deg,#c9b8a8,#6f6258)"></div>
    <div class="acc-name">Felix Moreno</div>
    <div class="acc-tags"><svg width="14" height="10" viewBox="0 0 14 10"><path d="M0 0h9l5 5-5 5H0z" fill="var(--green)"/></svg>Design, Devlopment</div>
    <div class="acc-time"><svg width="12" height="12" viewBox="0 0 12 12"><circle cx="6" cy="6" r="5" fill="none" stroke="#333" stroke-width="1.5"/><path d="M6 3v3h2" fill="none" stroke="#333" stroke-width="1.2"/></svg>This Week 1h:12m <svg width="8" height="5" viewBox="0 0 8 5"><path d="M1 1l3 3 3-3" fill="none" stroke="#777" stroke-width="1.3"/></svg></div>
    <div class="acc-actions"><svg width="11" height="12" viewBox="0 0 11 12"><path d="M1 3h9M4 1h3M2 3l1 8h5l1-8" fill="none" stroke="#aaa" stroke-width="1.3"/></svg>|<svg width="13" height="12" viewBox="0 0 13 12"><path d="M9 1H1v10h9V7M5 7l7-6" fill="none" stroke="#aaa" stroke-width="1.3"/></svg></div>
  </div>
  <div class="account-row">
    <div class="avatar" role="img" aria-label="Account holder photo" style="width:38px;height:38px;background:linear-gradient(135deg,#8a5fb0,#3a2a4a)"></div>
    <div class="acc-name">Nadia L. Brooks</div>
    <div class="acc-tags"><svg width="14" height="10" viewBox="0 0 14 10"><path d="M0 0h9l5 5-5 5H0z" fill="var(--green)"/></svg>Copywriting, Photography</div>
    <div class="acc-time"><svg width="12" height="12" viewBox="0 0 12 12"><circle cx="6" cy="6" r="5" fill="none" stroke="#333" stroke-width="1.5"/><path d="M6 3v3h2" fill="none" stroke="#333" stroke-width="1.2"/></svg>This Week 1h:12m <svg width="8" height="5" viewBox="0 0 8 5"><path d="M1 1l3 3 3-3" fill="none" stroke="#777" stroke-width="1.3"/></svg></div>
    <div class="acc-actions"><svg width="11" height="12" viewBox="0 0 11 12"><path d="M1 3h9M4 1h3M2 3l1 8h5l1-8" fill="none" stroke="#aaa" stroke-width="1.3"/></svg>|<svg width="13" height="12" viewBox="0 0 13 12"><path d="M9 1H1v10h9V7M5 7l7-6" fill="none" stroke="#aaa" stroke-width="1.3"/></svg></div>
  </div>
  <div class="account-row">
    <div class="avatar" role="img" aria-label="Account holder photo" style="width:38px;height:38px;background:linear-gradient(135deg,#9fb4c4,#4f5f6c)"></div>
    <div class="acc-name">Felix Moreno</div>
    <div class="acc-tags"><svg width="14" height="10" viewBox="0 0 14 10"><path d="M0 0h9l5 5-5 5H0z" fill="var(--green)"/></svg>Design, Devlopment</div>
    <div class="acc-time"><svg width="12" height="12" viewBox="0 0 12 12"><circle cx="6" cy="6" r="5" fill="none" stroke="#333" stroke-width="1.5"/><path d="M6 3v3h2" fill="none" stroke="#333" stroke-width="1.2"/></svg>This Week 1h:12m <svg width="8" height="5" viewBox="0 0 8 5"><path d="M1 1l3 3 3-3" fill="none" stroke="#777" stroke-width="1.3"/></svg></div>
    <div class="acc-actions"><svg width="11" height="12" viewBox="0 0 11 12"><path d="M1 3h9M4 1h3M2 3l1 8h5l1-8" fill="none" stroke="#aaa" stroke-width="1.3"/></svg>|<svg width="13" height="12" viewBox="0 0 13 12"><path d="M9 1H1v10h9V7M5 7l7-6" fill="none" stroke="#aaa" stroke-width="1.3"/></svg></div>
  </div>
</section>

<aside class="card sidebar">
  <nav class="tabs">
    <div class="tab is-active">Today</div>
    <div class="tab">Chat</div>
    <div class="tab">Activity</div>
  </nav>
  <div class="today">
    <div class="today-day">Wednesday</div>
    <div class="today-date">15<sup>th</sup> March</div>
  </div>
  <div class="events">
    <div class="section-title">Events</div>
    <div class="event is-hover">Group Meeting<small><svg width="9" height="9" viewBox="0 0 12 12"><circle cx="6" cy="6" r="5" fill="none" stroke="#999" stroke-width="1.6"/><path d="M6 3v3h2" fill="none" stroke="#999" stroke-width="1.4"/></svg>In 32 Minutes, Room 1B</small></div>
    <div class="event">Public Beta Release<small><svg width="9" height="9" viewBox="0 0 12 12"><circle cx="6" cy="6" r="5" fill="none" stroke="#999" stroke-width="1.6"/><path d="M6 3v3h2" fill="none" stroke="#999" stroke-width="1.4"/></svg>11:00 PM</small></div>
    <div class="event">Dinner with Marcus<small><svg width="9" height="9" viewBox="0 0 12 12"><circle cx="6" cy="6" r="5" fill="none" stroke="#999" stroke-width="1.6"/><path d="M6 3v3h2" fill="none" stroke="#999" stroke-width="1.4"/></svg>17:30 PM</small></div>
    <div class="event">Q&amp;A Session<small><svg width="9" height="9" viewBox="0 0 12 12"><circle cx="6" cy="6" r="5" fill="none" stroke="#999" stroke-width="1.6"/><path d="M6 3v3h2" fill="none" stroke="#999" stroke-width="1.4"/></svg>20:30 PM</small></div>
  </div>
  <div class="section-title">Notes</div>
  <div class="note">Best songs to listen while working<small>Last edit: May 8th, 2015</small></div>
  <div class="note">Useful subreddits<small>Last edit: January 12th, 2015</small></div>
  <div class="notify">Notifications Settings<span class="switch"></span></div>
</aside>

<footer class="footer">
  <span>© 2017 CareTrackr. All Rights Reserved</span>
  <span>Contact Us</span>
</footer>
</body>
</html>
```